Logo and animation for a set-top box for IPTV

We manufacture a set top box for IPTV. We need a better looking new boot up sequence. The process looks like that:
1. Logo (KV520/KV620/KV720) (needed in bot raster and vector)
2. "Loading" - here we want to have some kind of a better looking picture and and animation that consist of 30 frames- 30 separated image files.
3. "Waiting for network" screen should be changed to be with same design of the previous two screens. We must keep the bottom text too.

All images are 1920х1080

Attaching our current images.

As on the attached pictures.

```html
<!DOCTYPE html>
<html lang="en">
<head>
<meta charset="utf-8">
<title>Waiting for Network – Boot Sequence Frames</title>
<link rel="stylesheet" href="https://fonts.googleapis.com/css2?family=Exo+2:ital,wght@1,700;1,800&display=swap">
<style>
  :root {
    --page: #ffffff;
    --screen: #05090a;
    --ink: #ffffff;
    --accent: #1f6fb8;
    --accent-dim: #1a4a78;
    --accent-faint: #2a3440;
    --label: #111111;
  }
  html, body {
    margin: 0;
    width: 1200px;
    height: 1200px;
    overflow: hidden;
    background: var(--page);
  }
  .stage {
    position: relative;
    width: 1080px;
    height: 1080px;
    transform: scale(1.11111);
    transform-origin: 0 0;
    font-family: "Exo 2", "Arial Narrow", sans-serif;
  }
  .sequence-label {
    position: absolute;
    margin: 0;
    font-size: 15px;
    font-weight: 800;
    font-style: italic;
    font-variant: small-caps;
    letter-spacing: 0.2px;
    color: var(--label);
    text-transform: lowercase;
  }
  .sequence-label--first { left: 10px; top: 26px; }
  .sequence-label--last { left: 985px; top: 1032px; }
  .timeline {
    position: absolute;
    left: 0;
    top: 0;
  }
  .screen {
    position: absolute;
    top: 30px;
    width: 413px;
    height: 1018px;
    background: var(--screen);
  }
  .screen--intro { left: 108px; }
  .screen--outro { left: 560px; }
  .frame {
    position: absolute;
    left: 93px;
    height: 24px;
    white-space: nowrap;
  }
  .status {
    position: relative;
    display: inline-block;
    margin: 0;
    font-size: 23px;
    line-height: 24px;
    font-weight: 800;
    font-style: italic;
    font-variant: small-caps;
    letter-spacing: -0.3px;
    color: var(--ink);
  }
  .status__sweep {
    position: absolute;
    left: 0;
    top: 0;
    color: var(--accent);
    clip-path: inset(58% var(--to-right, 100%) 0 var(--from-left, 0));
  }
  .dots {
    position: absolute;
    left: 213px;
    top: 16px;
    display: flex;
    gap: 4px;
  }
  .dot {
    width: 4px;
    height: 4px;
    border-radius: 50%;
    background: var(--accent);
  }
  .dot--dim { background: var(--accent-dim); }
  .dot--faint { background: var(--accent-faint); }
  .dot--empty { background: transparent; }
  .settings-hint {
    position: absolute;
    left: 0;
    right: 0;
    bottom: 5px;
    text-align: center;
    color: var(--accent);
  }
  .settings-hint__icon {
    display: block;
    margin: 0 auto 3px;
  }
  .settings-hint__text {
    margin: 0;
    font-size: 6px;
    font-weight: 800;
    font-style: italic;
    letter-spacing: 0.2px;
  }
</style>
</head>
<body>
<div class="stage">
  <p class="sequence-label sequence-label--first">1st Frame</p>
  <p class="sequence-label sequence-label--last">Last Frame</p>

  <svg class="timeline" width="1080" height="1080" aria-hidden="true">
    <g stroke="#111" stroke-width="1" fill="none">
      <line x1="90" y1="62" x2="90" y2="1048"/>
      <line x1="90" y1="1048" x2="85" y2="1036"/>
      <line x1="985" y1="30" x2="985" y2="1015"/>
      <line x1="985" y1="1015" x2="990" y2="1004"/>
    </g>
  </svg>

  <section class="screen screen--intro">
    <div class="frame" style="top:103px">
      <p class="status">Waiting for Network</p>
    </div>
    <div class="frame" style="top:260px">
      <p class="status">Waiting for Network<span class="status__sweep" aria-hidden="true" style="--from-left:0;--to-right:78%">Waiting for Network</span></p>
    </div>
    <div class="frame" style="top:417px">
      <p class="status">Waiting for Network<span class="status__sweep" aria-hidden="true" style="--from-left:0;--to-right:40%">Waiting for Network</span></p>
    </div>
    <div class="frame" style="top:574px">
      <p class="status">Waiting for Network<span class="status__sweep" aria-hidden="true" style="--from-left:0;--to-right:0">Waiting for Network</span></p>
    </div>
    <div class="frame" style="top:731px">
      <p class="status">Waiting for Network<span class="status__sweep" aria-hidden="true" style="--from-left:38%;--to-right:0">Waiting for Network</span></p>
    </div>
    <div class="frame" style="top:888px">
      <p class="status">Waiting for Network<span class="status__sweep" aria-hidden="true" style="--from-left:81%;--to-right:0">Waiting for Network</span></p>
    </div>
    <div class="settings-hint">
      <svg class="settings-hint__icon" width="12" height="12" viewBox="0 0 12 12" aria-hidden="true">
        <circle cx="6" cy="6" r="5" fill="none" stroke="currentColor" stroke-width="0.8"/>
        <circle cx="6" cy="6" r="2.2" fill="none" stroke="currentColor" stroke-width="0.8"/>
      </svg>
      <p class="settings-hint__text">PRESS FOR SETTINGS</p>
    </div>
  </section>

  <section class="screen screen--outro">
    <div class="frame" style="top:103px">
      <p class="status">Waiting for Network</p>
      <span class="dots" aria-hidden="true"><span class="dot"></span></span>
    </div>
    <div class="frame" style="top:260px">
      <p class="status">Waiting for Network</p>
      <span class="dots" aria-hidden="true"><span class="dot dot--dim"></span><span class="dot"></span></span>
    </div>
    <div class="frame" style="top:417px">
      <p class="status">Waiting for Network</p>
      <span class="dots" aria-hidden="true"><span class="dot dot--faint"></span><span class="dot dot--dim"></span><span class="dot"></span></span>
    </div>
    <div class="frame" style="top:574px">
      <p class="status">Waiting for Network</p>
      <span class="dots" aria-hidden="true"><span class="dot dot--empty"></span><span class="dot dot--dim"></span><span class="dot dot--dim"></span></span>
    </div>
    <div class="frame" style="top:731px">
      <p class="status">Waiting for Network</p>
      <span class="dots" aria-hidden="true"><span class="dot dot--empty"></span><span class="dot dot--empty"></span><span class="dot dot--faint"></span></span>
    </div>
    <div class="frame" style="top:888px">
      <p class="status">Waiting for Network</p>
    </div>
    <div class="settings-hint">
      <svg class="settings-hint__icon" width="12" height="12" viewBox="0 0 12 12" aria-hidden="true">
        <circle cx="6" cy="6" r="5" fill="none" stroke="currentColor" stroke-width="0.8"/>
        <circle cx="6" cy="6" r="2.2" fill="none" stroke="currentColor" stroke-width="0.8"/>
      </svg>
      <p class="settings-hint__text">PRESS FOR SETTINGS</p>
    </div>
  </section>
</div>
</body>
</html>
```